ReelKindra.com - Landing Page

I need a Landing Page to present ReelKindra.com. It is a Platform that will allow people to COLLABORATE to produce Video Projects (Movies, Documentaries, Tv Shows etc).

As I described in the comments AT THE BEGINNING there will be just one Social Movie (is how we call a Video Project) featured in the Landing Page and others will follow.

In the Landing Page I need just the BASIC features of a WebSite to keep contact with who is interested in the Project (email contact etc).
Updates

Project Deadline Extended
Reason: Dears in the last few days several designers showed interest in submitting a Design for this project. I think is better if I give few days more for them to prepare their submissions. So I extended the deadline for 7 days Thanks Tomas

Target Market(s)

Wannabe Video Directors/ Producers around the world

Industry/Entity Type

Movie

Requirements
Must have
• a) Designed to be ready for Responsive Web Design.

b) Landing Page with possible infinite Scrolling

c) At the Centre of the Page there must the Space for to embed an image that is a link to another WebSite that is under construction. This other WebSite is the first Experiment of a Collaborative Video Production over the Web

d) Even if the ReelKindra Logo is in Black and White (see below 2 versions) there is no need that the Site is in Black and White. The colors fit the Logo
Should not have
• a) Parallax

```html
<!DOCTYPE html>
<html lang="en">
<head>
<meta charset="utf-8">
<title>ReelKindra.com</title>
<link rel="stylesheet" href="https://fonts.googleapis.com/css2?family=Arimo:ital,wght@0,400;0,700;1,400&display=swap">
<style>
  :root {
    --page-bg: #ffffff;
    --brand-blue: #1a4a8a;
    --bar-top: #2560a3;
    --bar-bottom: #174a88;
    --text-body: #4a4a4a;
    --text-muted: #5a5a5a;
    --player-dark: #3a3a3a;
    --player-edge: #2a2a2a;
    --controls: #1c1c1c;
    --frame-border: #dcdcdc;
  }
  * { box-sizing: border-box; margin: 0; padding: 0; }
  html, body {
    width: 1200px; height: 1024px; overflow: hidden;
    background: var(--page-bg);
    font-family: "Arimo", Arial, sans-serif;
  }
  .page { position: relative; width: 1200px; height: 1024px; }

  .brand {
    position: absolute; top: 178px; left: 0; width: 1200px;
    text-align: center;
    font-weight: 700; font-size: 34px; letter-spacing: -0.5px;
    color: var(--brand-blue);
  }

  .intro {
    position: absolute; top: 266px; left: 260px; width: 690px;
    text-align: center; font-size: 13px; line-height: 17px;
    color: var(--text-body);
  }

  .player-shadow {
    position: absolute; top: 628px; left: 318px; width: 546px; height: 60px;
    background: radial-gradient(ellipse at 50% 50%, rgba(0,0,0,0.45) 0%, rgba(0,0,0,0.15) 45%, rgba(0,0,0,0) 70%);
  }
  .player-frame {
    position: absolute; top: 389px; left: 381px; width: 427px; height: 301px;
    background: #fff; border: 1px solid var(--frame-border); border-radius: 9px;
    box-shadow: 0 1px 3px rgba(0,0,0,0.15);
  }
  .player-screen {
    position: absolute; top: 10px; left: 7px; width: 412px; height: 282px;
    background: radial-gradient(ellipse at 50% 50%, #4a4a4a 0%, var(--player-dark) 55%, var(--player-edge) 100%);
    border-top: 3px solid #555;
    overflow: hidden;
  }
  .play-button {
    position: absolute; top: 111px; left: 191px; width: 48px; height: 48px;
    border-radius: 8px;
    background: linear-gradient(#f2f2f2, #a8a8a8);
    box-shadow: 0 4px 10px rgba(0,0,0,0.5);
  }
  .play-button svg { position: absolute; top: 12px; left: 14px; }
  .controls {
    position: absolute; bottom: 0; left: 0; width: 100%; height: 22px;
    background: linear-gradient(#262626, #111);
    border-top: 3px solid #555;
    color: #ddd; font-size: 7px;
  }
  .controls .scrub {
    position: absolute; top: -6px; left: 2px; width: 9px; height: 9px;
    border-radius: 50%; background: #ddd;
  }
  .controls .time { position: absolute; top: 6px; left: 65px; }
  .controls .time span { color: #888; }
  .controls .quality { position: absolute; top: 6px; right: 27px; color: #aaa; }
  .controls svg { position: absolute; }

  .columns {
    position: absolute; top: 779px; left: 166px; width: 880px;
    display: flex; justify-content: space-between;
  }
  .column {
    width: 392px; font-size: 9.5px; line-height: 11px; color: var(--text-muted);
  }

  .footer-shadow {
    position: absolute; top: 922px; left: 70px; width: 1060px; height: 30px;
    background: radial-gradient(ellipse at 50% 40%, rgba(0,0,0,0.35) 0%, rgba(0,0,0,0) 70%);
  }
  .footer-bar {
    position: absolute; top: 912px; left: 120px; width: 958px; height: 29px;
    background: linear-gradient(var(--bar-top), var(--bar-bottom));
    border-top: 1px solid #5f8ac0;
    color: #fff; font-size: 10px;
  }
  .footer-nav { position: absolute; top: 8px; left: 23px; font-weight: 700; }
  .footer-legal { position: absolute; top: 8px; right: 13px; font-style: italic; }
  .copyright {
    position: absolute; top: 967px; left: 0; width: 1200px;
    text-align: center; font-size: 9px; font-style: italic; color: var(--text-muted);
  }
</style>
</head>
<body>
<main class="page">
  <h1 class="brand">ReelKindra</h1>

  <p class="intro">Lorem ipsum dolor sit amet, consectetur adipisicing elit, sed do eiusmod tempor incididunt ut labore et dolore magna aliqua. Ut enim ad minim veniam, quis nostrud exercitation ullamco laboris nisi ut aliquip ex ea commodo consequat. Duis aute irure dolor in reprehenderit in voluptate velit esse cillum dolore eu fugiat nulla pariatur. Excepteur sint occaecat cupidatat non proident, sunt in culpa qui officia deserunt mollit anim id est laborum.</p>

  <div class="player-shadow"></div>
  <div class="player-frame">
    <div class="player-screen">
      <div class="play-button">
        <svg width="22" height="24" viewBox="0 0 22 24"><path d="M2 1 L21 12 L2 23 Z" fill="#fff" stroke="#888" stroke-width="1.5"/></svg>
      </div>
      <div class="controls">
        <div class="scrub"></div>
        <svg style="top:5px;left:15px" width="10" height="10" viewBox="0 0 10 10"><path d="M1 0 L9 5 L1 10 Z" fill="#999"/></svg>
        <svg style="top:5px;left:42px" width="12" height="10" viewBox="0 0 12 10"><path d="M0 3 H3 L7 0 V10 L3 7 H0 Z" fill="#999"/><path d="M9 2 Q11 5 9 8" stroke="#999" fill="none"/></svg>
        <div class="time">0:00 <span>/ 4:20</span></div>
        <svg style="top:6px;right:50px" width="11" height="9" viewBox="0 0 11 9"><path d="M0 0 H11 V6 H4 L2 9 V6 H0 Z" fill="#c0302a"/></svg>
        <div class="quality">360p</div>
        <svg style="top:5px;right:7px" width="10" height="10" viewBox="0 0 10 10" fill="none" stroke="#999"><path d="M0 3 V0 H3 M7 0 H10 V3 M10 7 V10 H7 M3 10 H0 V7"/></svg>
      </div>
    </div>
  </div>

  <section class="columns">
    <p class="column">Lorem ipsum dolor sit amet, consectetur adipisicing elit, sed do eiusmod tempor incididunt ut labore et dolore magna aliqua. Ut enim ad minim veniam, quis nostrud exercitation ullamco laboris nisi ut aliquip ex ea commodo consequat. Duis aute irure dolor in reprehenderit in voluptate velit esse cillum dolore eu fugiat nulla pariatur. Excepteur sint occaecat cupidatat non proident, sunt in culpa qui officia deserunt mollit anim id est laborum.</p>
    <p class="column">Lorem ipsum dolor sit amet, consectetur adipisicing elit, sed do eiusmod tempor incididunt ut labore et dolore magna aliqua. Ut enim ad minim veniam, quis nostrud exercitation ullamco laboris nisi ut aliquip ex ea commodo consequat. Duis aute irure dolor in reprehenderit in voluptate velit esse cillum dolore eu fugiat nulla pariatur. Excepteur sint occaecat cupidatat non proident, sunt in culpa qui officia deserunt mollit anim id est laborum.</p>
  </section>

  <div class="footer-shadow"></div>
  <footer class="footer-bar">
    <nav class="footer-nav">Home &nbsp;|&nbsp; Lorem Ipsum | Consectetur &nbsp;|&nbsp; Adipiscing &nbsp;|&nbsp; Elit</nav>
    <div class="footer-legal">Terms of Use | Privacy Policy</div>
  </footer>
  <p class="copyright">Copyright © ReelKindra 2013. &nbsp;All Rights Reserved</p>
</main>
</body>
</html>
```